Fernlake Business Card Design

We are looking for a fresh business card design for our new logo. We would like a business card that is unique but friendly. We are in the window coverings business offering blinds, shutters and shades for homes.

Target Market(s)

Targeting the end-consumer

Industry/Entity Type

Business

Requirements
Must have
• Must have a dedicates space for a photo of our sales person. Must contain our new logo (attached).

```html
<!DOCTYPE html>
<html lang="en">
<head>
<meta charset="utf-8">
<title>Fernlake Business Card</title>
<link href="https://fonts.googleapis.com/css2?family=Roboto:wght@400;700;900&display=swap" rel="stylesheet">
<style>
  :root {
    --bg: #ecebe8;
    --card: #f4f4f3;
    --card-back: #e2e2e2;
    --ink: #1d1d1f;
    --logo-grey: #4a4a4f;
    --green: #6ab534;
  }
  * { margin: 0; padding: 0; box-sizing: border-box; }
  html, body { width: 1200px; height: 1200px; overflow: hidden; }
  body {
    background: var(--bg);
    font-family: "Roboto", Arial, sans-serif;
    color: var(--ink);
    position: relative;
  }
  .card {
    position: absolute;
    left: 150px;
    width: 900px;
    height: 514px;
    border-radius: 28px;
    box-shadow: 0 6px 18px rgba(0,0,0,0.15);
    overflow: hidden;
  }
  .card-back {
    top: 60px;
    background: linear-gradient(135deg, #d6d6d6 0%, #ececec 55%, #dcdcdc 100%);
  }
  .brand {
    position: absolute;
    left: 0; right: 0; top: 170px;
    display: flex;
    align-items: center;
    justify-content: center;
    gap: 30px;
  }
  .brand-square {
    width: 110px; height: 110px;
    border: 8px solid var(--logo-grey);
    border-radius: 16px;
  }
  .brand-name {
    font-size: 120px;
    font-weight: 400;
    color: var(--logo-grey);
    letter-spacing: 1px;
    line-height: 1;
  }
  .tagline {
    position: absolute;
    left: 0; right: 0; top: 400px;
    text-align: center;
    font-size: 20px;
    letter-spacing: 1px;
  }
  .card-front {
    top: 630px;
    background: var(--card);
  }
  .photo {
    position: absolute;
    left: 95px; top: 70px;
    width: 250px; height: 275px;
    background: linear-gradient(180deg, #c9a58e 0%, #b04a5a 45%, #c9c2c6 100%);
    border-radius: 4px 4px 0 0;
  }
  .rule {
    position: absolute;
    left: 0; top: 345px;
    width: 840px; height: 7px;
    background: var(--green);
  }
  .details {
    position: absolute;
    left: 430px; top: 105px;
  }
  .name {
    font-size: 34px;
    font-weight: 900;
    color: var(--green);
    letter-spacing: 1px;
    margin-bottom: 8px;
  }
  .role {
    font-size: 21px;
    line-height: 1.3;
    letter-spacing: 0.5px;
    margin-bottom: 18px;
  }
  .contact-list { list-style: none; }
  .contact-list li {
    display: flex;
    align-items: center;
    gap: 20px;
    font-size: 23px;
    letter-spacing: 1px;
    height: 40px;
  }
  .contact-list svg { width: 24px; height: 24px; flex: none; }
  .address {
    position: absolute;
    left: 0; right: 0; top: 410px;
    text-align: center;
    font-size: 24px;
    letter-spacing: 1px;
  }
</style>
</head>
<body>
  <section class="card card-back">
    <div class="brand">
      <span class="brand-square"></span>
      <span class="brand-name">Fernlake</span>
    </div>
    <p class="tagline">Website or tagline goes here</p>
  </section>

  <section class="card card-front">
    <div class="photo" role="img" aria-label="Photo of the sales person"></div>
    <div class="rule"></div>
    <div class="details">
      <h1 class="name">DALE MORGAN</h1>
      <p class="role">Master Business Coach<br>and Creator of The BrightPath Method</p>
      <ul class="contact-list">
        <li>
          <svg viewBox="0 0 24 24" aria-hidden="true"><path fill="var(--green)" d="M6.6 10.8c1.4 2.8 3.8 5.1 6.6 6.6l2.2-2.2c.3-.3.7-.4 1-.2 1.1.4 2.3.6 3.6.6.6 0 1 .4 1 1V20c0 .6-.4 1-1 1C10.6 21 3 13.4 3 4c0-.6.4-1 1-1h3.5c.6 0 1 .4 1 1 0 1.3.2 2.5.6 3.6.1.3 0 .7-.2 1z"/></svg>
          555.210.4837
        </li>
        <li>
          <svg viewBox="0 0 24 24" aria-hidden="true"><rect x="2" y="5" width="20" height="14" rx="1" fill="var(--green)"/><path d="M2.5 5.5 12 13l9.5-7.5" fill="none" stroke="#fff" stroke-width="1.6"/></svg>
          info@fernlake.com
        </li>
        <li>
          <svg viewBox="0 0 24 24" aria-hidden="true"><circle cx="12" cy="12" r="10" fill="var(--green)"/><path d="M2 12h20M12 2c3 3 3 17 0 20M12 2c-3 3-3 17 0 20" fill="none" stroke="#fff" stroke-width="1.3"/></svg>
          www.fernlake.com
        </li>
      </ul>
    </div>
    <p class="address">P.O. Box 418260, Aspen Hollow, CO 80000</p>
  </section>
</body>
</html>
```